Dental Practice - Smiles Ahead - Corvell Walk - requires New Patient Flyer

We need a flyer to tell prospecting new patients about a new patient offer in our practice, Themed with black and whitewith a bit of colour, and using black and white stripes if possible.
We want to look empathetic, modern and appeal to adults.
The offer is for a complete comprehensive dental examination including all necessary x-rays with no out of pocket expense

Target Market(s)

adults, in particular 30-60 year olds

Industry/Entity Type

Dental

Font styles to use
Sans Serif

Colors
000000
ffffff
cee9f5

Requirements
Must have
• Smiles Ahead
• We are located in the heart of city Adelaide, along the iconic Corvell Walk.
• Dentist
• Complete comprehensive dental examination including all necessary x-rays
• with $0 out of pocket expense if you have dental health cover.
• No Health fund? We will do it all for you $95.
• With over 50 years combined experience, Dr Peter Halvorsen and Dr Wesley Tunbridge can offer all areas of dental treatment including Preventative, Whitening, Children, General, Cosmetic, Removal, Sedation and Implants.
• (08) 8564 3097
• frontdesk@brightquaydental.com.au
• Level 2, 17 Corvell Walk Adelaide SA 5000
• Please try and include all 3 pictures attached
Nice to have
• Partner Plus with KOVA, Accept all health funds, claim on the spot with MEDSWIPE
Should not have
• colour red, someone not smiling, someone in pain, photo of bad teeth/smile

```html
<!DOCTYPE html>
<html lang="en">
<head>
<meta charset="utf-8">
<title>Smiles Ahead – New Patient Flyer</title>
<link href="https://fonts.googleapis.com/css2?family=Arimo:ital,wght@0,400;0,700;1,700&family=Archivo+Black&family=Tinos:wght@400;700&display=swap" rel="stylesheet">
<style>
  :root {
    --black: #000000;
    --ink: #1a1a1a;
    --white: #ffffff;
    --ice: #cee9f5;
    --stripe: #e4f1f9;
    --sky-deep: #2f6fbf;
    --sky-mid: #4f93d6;
    --sky-light: #a9d0ee;
    --fund-blue: #1a9ad8;
    --backdrop: #2a2a2a;
  }
  * { margin: 0; padding: 0; box-sizing: border-box; }
  html, body { width: 1079px; height: 1200px; overflow: hidden; }
  body { background: var(--backdrop); font-family: "Arimo", Arial, sans-serif; position: relative; }

  .flyer { position: absolute; left: 170px; top: 80px; width: 738px; height: 1040px; background: var(--white); overflow: hidden; }
  .bar { position: absolute; left: 0; width: 100%; background: var(--black); }
  .bar--top { top: 0; height: 32px; }
  .bar--bottom { top: 1026px; height: 14px; }

  .hero { position: absolute; left: 0; top: 32px; width: 738px; height: 274px;
    background: linear-gradient(100deg, var(--sky-deep) 0%, var(--sky-mid) 45%, var(--sky-light) 75%, #dcecf7 100%); }
  .hero__photo { position: absolute; left: 454px; top: 0; width: 284px; height: 274px;
    background: linear-gradient(160deg, #c9dff0 0%, #9a7a66 45%, #5a3f33 100%); }
  .hero__tagline { position: absolute; left: 46px; top: 32px; color: var(--white); font-size: 24px; }
  .hero__tagline strong { font-family: "Archivo Black", sans-serif; font-weight: 400; }
  .hero__tagline-sub { position: absolute; left: 210px; top: 74px; color: var(--white); font-size: 20px; }
  .brand { position: absolute; left: 46px; top: 146px; width: 400px; height: 100px; color: var(--white); font-weight: 400; }
  .brand__small { position: absolute; left: 0; top: 40px; font-size: 40px; line-height: 1; }
  .brand__large { position: absolute; left: 124px; top: 0; font-family: "Tinos", "Times New Roman", serif; font-size: 88px; line-height: 1; white-space: nowrap; }

  .offer { position: absolute; left: 0; top: 306px; width: 426px; height: 494px;
    background: repeating-linear-gradient(90deg, var(--white) 0 6px, var(--stripe) 6px 9px); }
  .offer__cover { position: absolute; left: 53px; top: 38px; font-size: 28px; font-weight: 700; line-height: 35px; color: var(--ink); }
  .offer__nofund { position: absolute; left: 53px; top: 206px; font-family: "Archivo Black", sans-serif; font-size: 46px; line-height: 48px; color: var(--ink); }
  .offer__price { position: absolute; left: 53px; top: 306px; font-size: 35px; font-weight: 700; line-height: 41px; color: var(--ink); }
  .fund { position: absolute; left: 54px; top: 396px; display: flex; align-items: flex-start; gap: 14px; }
  .fund__badge { width: 72px; }
  .fund__square { width: 72px; height: 62px; background: var(--fund-blue); }
  .fund__name { font-size: 8px; font-weight: 700; color: var(--fund-blue); margin-top: 3px; white-space: nowrap; letter-spacing: 0.2px; }
  .fund__note { font-family: "Tinos", serif; font-size: 17px; line-height: 21px; color: var(--ink); margin-top: 34px; white-space: nowrap; }

  .team { position: absolute; left: 426px; top: 306px; width: 312px; height: 494px; background: var(--ice); }
  .team__over { position: absolute; left: 32px; top: 8px; font-size: 36px; color: var(--ink); line-height: 1; }
  .team__years { position: absolute; left: 32px; top: 46px; font-family: "Archivo Black", sans-serif; font-size: 31px; line-height: 33px; color: var(--ink); }
  .team__doctors { position: absolute; left: 0; top: 158px; width: 312px; height: 63px; background: var(--ink); color: var(--white); font-size: 18px; font-weight: 700; line-height: 22px; padding: 12px 0 0 32px; }
  .team__heading { position: absolute; left: 32px; top: 236px; font-size: 25px; font-weight: 400; line-height: 26px; color: var(--ink); }
  .treatments { position: absolute; left: 32px; top: 294px; list-style: none; display: grid; grid-template-columns: 142px 140px; font-size: 18px; font-weight: 700; line-height: 23px; color: var(--ink); }
  .treatments li::before { content: "• "; }
  .treatments .wide { grid-column: 1 / 3; }
  .team__rule { position: absolute; left: 0; top: 389px; width: 312px; height: 1px; background: #6b7f8a; }
  .team__exam { position: absolute; left: 32px; top: 400px; font-size: 17px; font-weight: 700; font-style: italic; line-height: 20px; color: var(--ink); }

  .location { position: absolute; left: 0; top: 800px; width: 738px; height: 36px; background: var(--black); color: var(--white); font-size: 18px; font-weight: 700; text-align: center; line-height: 36px; }

  .contact { position: absolute; left: 0; top: 836px; width: 738px; height: 190px; background: var(--ice); }
  .contact__phone { position: absolute; left: 50px; top: 20px; font-family: "Tinos", serif; font-weight: 700; font-size: 54px; color: var(--ink); line-height: 1; }
  .contact__email, .contact__address { position: absolute; left: 56px; font-size: 17px; font-weight: 700; color: var(--ink); }
  .contact__email { top: 92px; }
  .contact__address { top: 118px; }
  .contact__map { position: absolute; left: 450px; top: 16px; width: 260px; height: 162px; background: linear-gradient(135deg, #bcdcec, #a8cfe3); }
</style>
</head>
<body>
  <main class="flyer">
    <div class="bar bar--top"></div>

    <header class="hero">
      <p class="hero__tagline">Get <strong>“WOW”</strong> Whitening</p>
      <p class="hero__tagline-sub">Results, Today.</p>
      <h1 class="brand">
        <span class="brand__small">Smiles</span>
        <span class="brand__large">Ahead</span>
      </h1>
      <div class="hero__photo" role="img" aria-label="Photo of a smiling young woman with long brown hair"></div>
    </header>

    <section class="offer">
      <p class="offer__cover">With $0 Out of<br>Pocket Expense<br>If you have<br>Dental Health Cover</p>
      <p class="offer__nofund">No Health<br>Fund?</p>
      <p class="offer__price">We will do it<br>All for You $95</p>
      <div class="fund">
        <div class="fund__badge">
          <div class="fund__square"></div>
          <div class="fund__name">KOVA PARTNER PLUS</div>
        </div>
        <p class="fund__note">Accept All Health Funds,<br>Claim On The Spot with MEDSWIPE</p>
      </div>
    </section>

    <section class="team">
      <p class="team__over">Over</p>
      <p class="team__years">50 Years<br>Combined<br>Experience</p>
      <p class="team__doctors">Dr Peter Halvorsen &amp;<br>Dr Wesley Tunbridge</p>
      <h2 class="team__heading">Offer All Areas of<br>Dental Treatment</h2>
      <ul class="treatments">
        <li>Preventative</li><li>Whitening</li>
        <li>Children</li><li>General</li>
        <li>Cosmetic</li><li>Removal</li>
        <li class="wide">Sedation and Implant</li>
      </ul>
      <div class="team__rule"></div>
      <p class="team__exam">Complete Comprehensive<br>Dental Examination<br>Including All<br>Necessary x-rays</p>
    </section>

    <p class="location">We are located in the heart of city Adelaide, along the iconic Corvell Walk</p>

    <footer class="contact">
      <p class="contact__phone">(08) 8564 3097</p>
      <p class="contact__email">frontdesk@brightquaydental.com.au</p>
      <p class="contact__address">Level 2, 17 Corvell Walk Adelaide SA 5000</p>
      <div class="contact__map" role="img" aria-label="Street map showing the practice location on Corvell Walk"></div>
    </footer>

    <div class="bar bar--bottom"></div>
  </main>
</body>
</html>
```